Velvora Beauty Sensitive Skin Intimate Shave Cream

We need a label/package design for a female shave cream. Our brand is Velvora Beauty and we manufacturer luxuriously sexy female intimate items. We are looking for sexy packaging to really get our brand out there. I have included in attachments, all of the files including font, logo, size requirements and verbage requirements. On the file "shave-cream-requirements" please use to format for size. Also on that file, I need the "must have" verbage from my project brief laid out exactly the same. The name of the product is Velvora Beauty Classic Silken Intimate Shave Cream
Target Market(s)
Females who like luxury and feeling sexy
Industry/Entity Type
Manufacturer
Requirements
Must have
- Must have my velvora beauty logo. The scent for this cream is called "silken classic" Please put that one the label. Also the actual scent is "an array of light florals with a hint of baby powder" please put that in small letters on back of the label
- Must be Label Dimensions: 6.25h X 7.375w
- Must say "Intimate Shave Cream for Her".
- Must say - Fill Weight: 16 Fl. Oz. (480ml) ℮
- must say - Suggested use: Apply intimate shave cream where desired and glide razor over skin for smooth results
- Must say - Ingredient Deck:
- Water (Eau/Aqua), Cetyl Alcohol, Cetrimonium Bromide, Stearyl Alcohol, Hydroxyethylcellulose, Glyceryl Stearate, PEG-100 Stearate, PEG-60 Lanolin, Simmondsia Chinensis (Jojoba) Seed Oil, Hydrolyzed Keratin, Panthenol, Allantoin, Phenoxyethanol, Methylisothiazolinone, Sodium Hydroxide, Fragrance (Parfum)
- Must say these cautions:
- Recommend Cautions:
- Do Not Use if You have a Known Hypersensitivity (Allergy) to Any of the Ingredients
- If Irritation Occurs, Discontinue Use
- If Eye Contact Occurs, Rinse with Water to Remove
- Keep Out of Reach of Children
- Must say : Specially formulated with skin soothing ingredients to provide a smooth and effortless shave.
- Protects and nourishes from irritation and razor cuts
- Helps prevent embarrassing shave rashes and ingrown hairs.
- Designed for sensitive and intimate skin. Perfect for intimate areas, legs, underarms, face, and body.
- Enhanced with hair and skin moisturizing agents.
- Can also be used to condition skin and hair after shampoo.
- Must have UPC (included) and part number:VK584731 in small writing on the back of the label.
Should not have
- cheap looking designs and logos

```html
<!DOCTYPE html>
<html lang="en">
<head>
<meta charset="utf-8">
<title>Velvora Beauty Classic Silken Intimate Shave Cream – Label</title>
<link rel="stylesheet" href="https://fonts.googleapis.com/css2?family=Montserrat:wght@300;400;600&family=Great+Vibes&display=swap">
<style>
  :root {
    --plum-deep: #2a1420;
    --plum-mid: #3b1a2d;
    --plum-glow: #4a2038;
    --rose: #b23574;
    --rose-soft: #c45a8d;
    --text-head: #b9aab3;
    --text-body: #7d6a74;
    --text-bright: #e9dfe4;
    --ink: #1a0d14;
  }
  * { margin: 0; padding: 0; box-sizing: border-box; }
  html, body {
    width: 1200px; height: 1017px; overflow: hidden;
    background: var(--plum-deep);
    font-family: "Montserrat", Arial, sans-serif;
  }
  .label { position: relative; width: 1200px; height: 1017px; background: var(--plum-deep); }

  .panel-front {
    position: absolute; left: 326px; top: 0; width: 494px; height: 1017px;
    background: radial-gradient(ellipse at 50% 45%, var(--plum-glow) 0%, var(--plum-mid) 55%, var(--plum-deep) 100%);
  }
  .rule { position: absolute; top: 0; width: 3px; height: 1017px; background: var(--rose); }
  .rule--left { left: 323px; }
  .rule--right { left: 820px; }

  /* back panel */
  .back { position: absolute; left: 32px; width: 270px; color: var(--text-body); font-size: 13px; line-height: 1.3; }
  .back h3 { color: var(--text-head); font-size: 15px; font-weight: 600; margin-bottom: 2px; }
  .back h4 { color: var(--text-head); font-size: 11px; font-weight: 600; }
  .back .small { font-size: 10.5px; line-height: 1.3; margin-bottom: 14px; }
  .suggested { top: 146px; }
  .ingredients { top: 236px; }
  .cautions { top: 574px; }
  .cautions h3 { font-size: 14px; margin-bottom: 6px; }

  /* front panel */
  .brand {
    position: absolute; left: 326px; width: 494px; top: 70px; text-align: center;
    color: var(--text-bright); font-weight: 300;
  }
  .brand__name { font-size: 44px; letter-spacing: 18px; padding-left: 18px; }
  .brand__sub { font-size: 17px; letter-spacing: 7px; padding-left: 7px; margin-top: 4px; }
  .brand__line { width: 300px; height: 1px; background: var(--text-body); margin: 8px auto 0; }

  .ornament {
    position: absolute; left: 366px; top: 225px; width: 414px; height: 540px;
    border-radius: 48% 48% 40% 40%;
    background: radial-gradient(ellipse at 50% 45%, rgba(178,53,116,0.22) 0%, rgba(178,53,116,0.08) 55%, rgba(178,53,116,0) 75%);
  }

  .product { position: absolute; left: 326px; width: 494px; top: 318px; text-align: center; }
  .product__script { font-family: "Great Vibes", cursive; font-size: 66px; color: var(--text-bright); line-height: 1; }
  .product__type { font-size: 17px; color: var(--text-head); letter-spacing: 1px; margin-top: 8px; }
  .product__for { font-size: 24px; color: var(--text-bright); font-weight: 600; letter-spacing: 2px; margin-top: 6px; }

  .scent { position: absolute; left: 326px; width: 494px; top: 752px; text-align: center; }
  .scent__name { font-size: 24px; color: var(--rose); font-weight: 400; }
  .scent__note { font-size: 8.5px; color: var(--text-body); line-height: 1.35; margin-top: 10px; }

  .front-ingredients { position: absolute; left: 380px; top: 876px; font-size: 14px; color: var(--ink); font-weight: 600; }
  .fill { position: absolute; left: 326px; width: 494px; top: 918px; text-align: center; font-size: 15px; color: var(--text-bright); }
  .fill__e { margin-left: 130px; font-size: 17px; }

  /* side panel */
  .claims { position: absolute; left: 850px; top: 146px; width: 320px; }
  .claim { margin-bottom: 14px; }
  .claim h3 { color: var(--text-head); font-size: 15px; font-weight: 600; line-height: 1.25; }
  .claim p { color: var(--text-body); font-size: 13px; line-height: 1.3; }

  .sku { position: absolute; left: 880px; width: 250px; top: 820px; text-align: center; color: var(--text-bright); font-size: 17px; line-height: 1.8; }
</style>
</head>
<body>
<main class="label">
  <div class="panel-front"></div>
  <div class="rule rule--left"></div>
  <div class="rule rule--right"></div>

  <section class="back suggested">
    <h3>Suggested use:</h3>
    <p>Apply intimate shave cream where desired and glide razor over skin for smooth results</p>
  </section>

  <section class="back ingredients">
    <h3>Ingredient Deck:</h3>
    <p>Water (Eau/Aqua),<br>Cetyl Alcohol,<br>Cetrimonium Bromide,<br>Stearyl Alcohol,<br>Hydroxyethylcellulose,<br>Glyceryl Stearate,<br>PEG-100 Stearate,<br>PEG-60 Lanolin,<br>Simmondsia<br>Chinensis (Jojoba) Seed Oil,<br>Hydrolyzed Keratin, Panthenol,<br>Allantoin, Phenoxyethanol,<br>Methylisothiazolinone,<br>Sodium Hydroxide,<br>Fragrance (Parfum)</p>
  </section>

  <section class="back cautions">
    <h3>Recommend Cautions:</h3>
    <p class="small">Do Not Use if You have a Known Hypersensitivity (Allergy) to Any of the Ingredients</p>
    <h4>If Irritation Occurs,</h4>
    <p class="small">Discontinue Use</p>
    <h4>If Eye Contact Occurs,</h4>
    <p class="small">Rinse with Water to Remove</p>
    <h4>Keep Out of Reach of Children</h4>
  </section>

  <header class="brand">
    <div class="brand__name">VELVORA</div>
    <div class="brand__line"></div>
    <div class="brand__sub">BEAUTY</div>
  </header>

  <div class="ornament" role="img" aria-label="Decorative rose-toned floral flourish framing the product name"></div>

  <section class="product">
    <div class="product__script">intimate</div>
    <div class="product__type">SHAVE CREAM</div>
    <div class="product__for">FOR HER</div>
  </section>

  <section class="scent">
    <div class="scent__name">silken classic</div>
    <p class="scent__note">an array of light florals<br>with a hint of baby powder</p>
  </section>

  <div class="front-ingredients">Ingredients:</div>
  <div class="fill">16 fl. oz. (480 ml)<span class="fill__e">℮</span></div>

  <section class="claims">
    <div class="claim"><h3>Specially formulated</h3><p>with skin soothing ingredients to provide a smooth and effortless shave.</p></div>
    <div class="claim"><h3>Protects and nourishes</h3><p>from irritation and razor cuts</p></div>
    <div class="claim"><h3>Helps prevent embarrassing</h3><p>shave rashes and ingrown hairs.</p></div>
    <div class="claim"><h3>Designed for sensitive and intimate skin.</h3></div>
    <div class="claim"><h3>Perfect for intimate areas,</h3><p>legs, underarms, face, and body.</p></div>
    <div class="claim"><h3>Enhanced with hair and skin moisturizing agents.</h3></div>
    <div class="claim"><h3>Can also be used to condition skin and hair after shampoo.</h3></div>
  </section>

  <section class="sku">
    <div>UnAssigned</div>
    <div>Model: VK584731</div>
    <div>SKU: VK584731</div>
  </section>
</main>
</body>
</html>
```